Business card for web design company
Web. Graphics. Print
Business card for web design company - Communications and Media
Creative Brief
Simple
Lunar Orchard
None
tessa@lunarorchard.example
www.lunarorchard.example
Front of the business card will have the umbrella picture fading out just like the sample pdf with the image of the mask. The business card will be printed as a clear plastic just like the sample pdf of the mask so please fade it to a transparent design similar in size. I want the front to have just the words Lunar Orchard from my logo (not the logo itself) and the tagline: Web. Graphics. Print.
I'd like a similar design as the back of the mask business card in the sample pdf. It has to match the size of the design on the front. The logo can go at the top. Underneath, please use a similar icon system as in the pink sample pdf design. It will have my name 'Tessa Marwick', and 'Web. Graphics. Print' beside the contact icon. Under the phone icon, please insert my phone and email. Underneath, please place my website address. You can use your own icons or I can provide them. The colors are to be shades of blue from the umbrella, white, and the color from my logo. The purple business card design in the sample pdf is just for color variation and font ideas.
brovelmotion brovelmotion
Pls check your private messages
lOrchard lOrchard
Designs #1-6 is the best. Thank you for the other designs but I need it to look like the first 6.
Please put the umbrella picture on the front, fading into transparent edge like in the sample pdf. Please see instructions.

```html
<!DOCTYPE html>
<html lang="en">
<head>
<meta charset="utf-8">
<title>Lunar Orchard — Business Card</title>
<link href="https://fonts.googleapis.com/css2?family=Michroma&family=Montserrat:wght@400;600&display=swap" rel="stylesheet">
<style>
  :root {
    --backdrop: #3a3a3a;
    --card: #ffffff;
    --teal: #4cc3c0;
    --teal-deep: #3bb1ae;
    --swoosh: #9a9a9a;
    --ink-light: #ffffff;
  }
  * { box-sizing: border-box; margin: 0; padding: 0; }
  html, body { width: 1200px; height: 770px; overflow: hidden; }
  body {
    background: var(--backdrop);
    display: flex;
    align-items: center;
    justify-content: center;
    gap: 40px;
    font-family: "Montserrat", sans-serif;
  }
  .card {
    position: relative;
    width: 540px;
    height: 309px;
    background: var(--card);
    border-radius: 14px;
    overflow: hidden;
  }
  /* Front */
  .card-front {
    display: flex;
    flex-direction: column;
    align-items: center;
    justify-content: center;
    gap: 16px;
  }
  .brand-dot {
    width: 58px;
    height: 58px;
    border-radius: 50%;
    background: var(--teal);
  }
  .brand-name {
    font-family: "Michroma", sans-serif;
    color: var(--teal);
    font-size: 22px;
    letter-spacing: 2px;
    text-transform: uppercase;
  }
  /* Back */
  .back-brand {
    position: absolute;
    top: 34px;
    left: 0;
    right: 0;
    display: flex;
    align-items: center;
    justify-content: center;
    gap: 18px;
  }
  .back-brand .brand-dot { width: 44px; height: 44px; }
  .back-brand .divider {
    width: 1px;
    height: 60px;
    background: var(--teal);
  }
  .back-brand .brand-name { font-size: 18px; }
  .band { position: absolute; inset: 0; }
  .contact {
    position: absolute;
    left: 0;
    right: 0;
    bottom: 26px;
    display: flex;
    justify-content: center;
    gap: 16px;
    color: var(--ink-light);
    font-size: 11px;
    line-height: 1.6;
  }
  .person { text-align: right; }
  .person-name { font-weight: 600; font-size: 13px; }
  .contact .divider {
    width: 1px;
    background: var(--ink-light);
    opacity: 0.8;
  }
  .contact-list { list-style: none; }
  .contact-list li { display: flex; align-items: center; gap: 7px; }
  .contact-list svg { width: 11px; height: 11px; flex: none; }
</style>
</head>
<body>

  <section class="card card-front" aria-label="Card front">
    <div class="brand-dot"></div>
    <div class="brand-name">Lunar Orchard</div>
  </section>

  <section class="card card-back" aria-label="Card back">
    <svg class="band" viewBox="0 0 540 309" preserveAspectRatio="none" aria-hidden="true">
      <path d="M0,150 Q260,118 540,128" fill="none" stroke="var(--swoosh)" stroke-width="3"/>
      <path d="M0,168 Q260,128 540,140 L540,309 L0,309 Z" fill="var(--teal)"/>
    </svg>

    <div class="back-brand">
      <div class="brand-dot"></div>
      <div class="divider"></div>
      <div class="brand-name">Lunar Orchard</div>
    </div>

    <div class="contact">
      <div class="person">
        <div class="person-name">Tessa Marwick</div>
        <div>Web. Graphics. Print</div>
        <div style="margin-top:22px">Suite 4, Elm Row,</div>
        <div>NY 10231</div>
      </div>
      <div class="divider"></div>
      <ul class="contact-list">
        <li>
          <svg viewBox="0 0 12 12"><path d="M3 1 L5 3.5 L4 5 Q5 7 7 8 L8.5 7 L11 9 L10 11 Q4 11 1 4 Z" fill="#fff"/></svg>
          123-456-7890
        </li>
        <li>
          <svg viewBox="0 0 12 12"><path d="M3 1 L5 3.5 L4 5 Q5 7 7 8 L8.5 7 L11 9 L10 11 Q4 11 1 4 Z" fill="#fff"/></svg>
          987-654-3210
        </li>
        <li>
          <svg viewBox="0 0 12 12"><path d="M3 1 L5 3.5 L4 5 Q5 7 7 8 L8.5 7 L11 9 L10 11 Q4 11 1 4 Z" fill="#fff"/></svg>
          456-789-1235
        </li>
        <li>
          <svg viewBox="0 0 12 12"><rect x="1" y="2.5" width="10" height="7" fill="none" stroke="#fff"/><path d="M1 2.5 L6 6.5 L11 2.5" fill="none" stroke="#fff"/></svg>
          tessa@lunarorchard.example
        </li>
        <li>
          <svg viewBox="0 0 12 12"><circle cx="6" cy="6" r="5" fill="none" stroke="#fff"/><path d="M1 6 H11 M6 1 Q3 6 6 11 M6 1 Q9 6 6 11" fill="none" stroke="#fff" stroke-width="0.8"/></svg>
          www.lunarorchard.example
        </li>
      </ul>
    </div>
  </section>

</body>
</html>
```